LanternPips business card for creator of IP TOY (fun) (children) designs

This business card will be the introduction of me as the creator of new designs to the toy industry and beyond. These designs are kept secret until being revealed one on one to each company. My design is patent pending protected IP. I am looking for business appropriate with a tinge of fun. Please no black backgounds as this is the toy industry. Be creative with the logo and colors please. Just imagine.

Target Market(s)

TOY Industry Executives - Inventor Relations - Manufacturers this is my first introduction card.

Industry/Entity Type

Toy Industry - I have included our Brand colors which can be seen on the cover of The Quiet Pebble Moon book so uses for any of these others colors would be intersting.

Contact Information for Business Card

LOGO Mara Delwyn Founder Creator 555 017 2869 4718 E Hollin Bend Fernhollow, QN 70812 www.lanternpips-demo.com maradelwyn@quillpost-mail.com Patent Pending IP

Font styles to use
Other font styles liked:
• The font used in the logo is Swiss721BT bold I need to see other fonts to be able to decide but need a clean look

Requirements
Must have
• A bit of an artistic flair although the logo is very simple. I am in the toy industry so would like something that sparks the look of being a creator?
Nice to have
• Please try a background other than stark white. Would like to see a play using brand colors?I like the logos which look like they are lifted off the page. Then under the logo the words (not lifted?) Any Action Any Character Any Teaching
Should not have
• No Black Backgrounds please! should look as clean as possible - I am not opposed to changing to a double sided card if that is more effectual.

```html
<!DOCTYPE html>
<html lang="en">
<head>
<meta charset="utf-8">
<title>LanternPips Business Card</title>
<link href="https://fonts.googleapis.com/css2?family=Roboto:wght@400;500;700&display=swap" rel="stylesheet">
<style>
  :root {
    --stage: #ece8e1;
    --card-green: #3f7563;
    --card-yellow: #f6e41c;
    --accent-yellow: #f3e23a;
    --logo-pale: #d6ecf5;
    --brand-red: #df2430;
    --ink-green: #2d6657;
  }
  * { margin: 0; padding: 0; box-sizing: border-box; }
  html, body { width: 1200px; height: 1014px; overflow: hidden; }
  body {
    background: var(--stage);
    font-family: 'Roboto', Arial, sans-serif;
    position: relative;
  }
  .card {
    position: absolute;
    width: 630px;
    height: 360px;
    border-radius: 6px;
    overflow: hidden;
    box-shadow: 0 14px 30px rgba(0,0,0,0.18);
  }
  .card--front {
    left: 100px;
    top: 110px;
    background: var(--card-green);
  }
  .card--back {
    left: 470px;
    top: 540px;
    background: var(--card-yellow);
  }
  .front__logo {
    position: absolute;
    left: 52px;
    top: 205px;
    font-weight: 500;
    font-size: 44px;
    color: var(--logo-pale);
    letter-spacing: -0.5px;
  }
  .front__details {
    position: absolute;
    left: 330px;
    top: 48px;
    color: var(--accent-yellow);
    font-size: 17px;
    line-height: 1.35;
  }
  .details__name { font-weight: 700; font-size: 22px; }
  .details__role { font-size: 22px; margin-bottom: 18px; }
  .details__note { margin-top: 18px; }
  .back__wordmark {
    position: absolute;
    left: 0;
    right: 0;
    top: 90px;
    text-align: center;
    font-weight: 500;
    font-size: 96px;
    line-height: 1;
    color: var(--brand-red);
    letter-spacing: -2px;
    white-space: nowrap;
  }
  .back__web {
    position: absolute;
    left: 40px;
    bottom: 30px;
    font-weight: 700;
    font-size: 24px;
    color: var(--ink-green);
  }
</style>
</head>
<body>
  <section class="card card--front" aria-label="Card front">
    <div class="front__logo">LanternPips</div>
    <div class="front__details">
      <div class="details__name">Mara Delwyn</div>
      <div class="details__role">Founder Creator</div>
      <div>555 017 2869</div>
      <div>maradelwyn@quillpost-mail.com</div>
      <div>4718 E Hollin Bend Fernhollow</div>
      <div>QN 70812</div>
      <div class="details__note">Patent Pending IP</div>
    </div>
  </section>

  <section class="card card--back" aria-label="Card back">
    <div class="back__wordmark">LanternPips</div>
    <div class="back__web">www.lanternpips-demo.com</div>
  </section>
</body>
</html>
```